I need a logo design for a new company based in Tucson called "Mindtrainer Lou Varga". I am a psychotherapist that specializes in clinical psychology with athletes and performers. The final design should incorporate the psychology symbol as a watermark. The logo should convey movement and fluidity. "Mindtrainer" is a bit of a play on words combining psychology (head) with sports (coach). Other design interests include mid-century, Gustav Orrin Pell. I will want to use the logo for business cards, letterhead and marketing brochures. I will put together a website at a later date. I am attaching a file with some pertinent information for the business card. Thank you.
Lou Varga
mindtrainerlouvarga@quellmail.net
Updates

Thank you all for the submissions so far.  I have submitted an additional file with a draft of a new design idea.  Since "mindtrainer" is a bit of a play on words, I would like to see something with the two "H's" look something like quotation marks.  If the psychology logo is to be included at all, it needs to be less prominent.     Thank you all.  Lou                               

Target Market(s)

1) Adolescent and adult athletes and performers who are looking to increase their level of performance (Sport and Performance Psychology)
2) Adult psychotherapy patients (Clinical psychology)

Industry/Entity Type

Marketing

Colors

Designer to choose colors to be used in the design.

Requirements
Must have
• 1) Since "mindtrainer" is a bit of a play on words, The "H's" need to be in a font that looks somewhat like quotation marks.

Nice to have
• Logo on one side. All other info on the backside?

```html
<!DOCTYPE html>
<html lang="en">
<head>
<meta charset="utf-8">
<title>Mindtrainer – Business Card</title>
<link href="https://fonts.googleapis.com/css2?family=Alegreya:wght@500&family=Lato:wght@400;700&display=swap" rel="stylesheet">
<style>
  :root {
    --bg: #c9c9c6;
    --card-top: #1c1c1c;
    --card-bottom: #0d0d0d;
    --green: #3d9a48;
    --white: #ffffff;
    --shadow: rgba(0, 0, 0, 0.35);
  }
  html, body {
    margin: 0;
    padding: 0;
    width: 1200px;
    height: 1000px;
    overflow: hidden;
    background: var(--bg);
  }
  .canvas {
    position: relative;
    width: 1200px;
    height: 1000px;
  }
  .card {
    position: absolute;
    width: 770px;
    height: 440px;
    border-radius: 22px;
    background: linear-gradient(160deg, var(--card-top), var(--card-bottom));
    box-shadow: 0 8px 18px var(--shadow);
    box-sizing: border-box;
  }
  .card--front {
    left: 330px;
    top: 50px;
  }
  .card--back {
    left: 100px;
    top: 520px;
    text-align: center;
    font-family: "Lato", sans-serif;
  }

  /* Front: brand name and tagline */
  .brand {
    position: absolute;
    left: 110px;
    top: 120px;
    width: 560px;
  }
  .brand__band {
    display: flex;
    align-items: center;
    gap: 22px;
    height: 128px;
    padding: 0 36px;
    border: 3px solid var(--green);
    box-sizing: border-box;
  }
  .brand__square {
    width: 44px;
    height: 44px;
    background: var(--green);
    flex: none;
  }
  .brand__name {
    font-family: "Lato", sans-serif;
    font-weight: 700;
    font-size: 66px;
    color: var(--white);
    letter-spacing: 1px;
  }
  .brand__tagline {
    margin-top: 12px;
    font-family: "Lato", sans-serif;
    font-weight: 400;
    font-size: 23px;
    letter-spacing: 2.5px;
    color: var(--white);
    text-transform: uppercase;
    white-space: nowrap;
  }

  /* Back: name and contact details */
  .holder {
    padding-top: 70px;
  }
  .holder__name {
    margin: 0;
    font-family: "Alegreya", serif;
    font-weight: 500;
    font-size: 46px;
    color: var(--green);
    letter-spacing: 0.5px;
  }
  .holder__title {
    margin: 2px 0 0;
    font-weight: 700;
    font-size: 20px;
    color: var(--white);
  }
  .contact {
    list-style: none;
    margin: 62px 0 0;
    padding: 0;
    font-size: 22px;
    line-height: 1.55;
    color: var(--white);
  }
  .contact__label {
    font-weight: 700;
    color: var(--green);
  }
</style>
</head>
<body>
<main class="canvas">
  <section class="card card--front" aria-label="Card front">
    <div class="brand">
      <div class="brand__band">
        <span class="brand__square" aria-hidden="true"></span>
        <span class="brand__name">Mindtrainer</span>
      </div>
      <div class="brand__tagline">Clinical &amp; Performance Psychology</div>
    </div>
  </section>

  <section class="card card--back" aria-label="Card back">
    <div class="holder">
      <h1 class="holder__name">Louis H. Varga, MA, LLC</h1>
      <p class="holder__title">Licensed Professional Counselor</p>
    </div>
    <ul class="contact">
      <li><span class="contact__label">Fax:</span> 520.555.0147</li>
      <li><span class="contact__label">Mobile:</span> 520.555.0182</li>
      <li><span class="contact__label">Email:</span> mindtrainerlouvarga@quellmail.net</li>
      <li><span class="contact__label">Address:</span> 4150 East Calder #210 Tucson, AZ 85712</li>
    </ul>
  </section>
</main>
</body>
</html>
```